Schedule Design - Attactive

I need my current schedule more attractive and able to print 3 foot x 4 foot. PSD Attached

We like how our schedule area is transparent and the times are blocked so you can see when they start and end

Target Market(s)

People that drink and cruise

Industry/Entity Type

Cruise Line

Requirements
Must have
• Bright colors, easy to see and read
Nice to have
• More legible times on the left
Should not have
• Dark colors

```html
<!DOCTYPE html>
<html lang="en">
<head>
<meta charset="utf-8">
<title>Coastal Country Sail Fest – Schedule</title>
<link href="https://fonts.googleapis.com/css2?family=Oswald:wght@400;600;700&display=swap" rel="stylesheet">
<style>
  :root{
    --page:#e9ecef;
    --sky-top:#1f9ad8;
    --sky-bottom:#c6e8f8;
    --wave:#1e6fb8;
    --tag:#8d969e;
    --tag-text:#ffffff;
    --fri:#f6ec17;
    --fri-event:#a6a21c;
    --sat:#3db54a;
    --sat-event:#1f8c3b;
    --sun:#e3262b;
    --sun-event:#a9181c;
    --line:rgba(255,255,255,.55);
    --ink:#2b2b2b;
    --white:#ffffff;
    --logo:#f7c21b;
    --ship:#e0504a;
    --row:27px;
  }
  *{box-sizing:border-box;margin:0;padding:0}
  html,body{width:724px;height:1200px;overflow:hidden;background:var(--page)}
  body{display:flex;align-items:center;justify-content:center;font-family:'Oswald',sans-serif}
  .schedule-board{position:relative;width:700px;height:525px;overflow:hidden;
    background:linear-gradient(180deg,var(--sky-top) 0%,var(--sky-bottom) 70%);}
  .waves{position:absolute;left:0;right:0;bottom:0;height:150px;
    background:linear-gradient(180deg,#4b9cd6,var(--wave));opacity:.75}
  .time-rail{position:absolute;left:12px;top:70px;width:64px}
  .time-tag{height:var(--row);display:flex;align-items:center}
  .time-tag span{display:block;width:50px;height:16px;line-height:16px;background:var(--tag);
    color:var(--tag-text);font-size:10px;padding-left:8px;letter-spacing:.5px;
    clip-path:polygon(0 0,82% 0,100% 50%,82% 100%,0 100%)}
  .day{position:absolute;top:17px;width:103px;height:493px}
  .day--fri{left:82px}.day--sat{left:191px}.day--sun{left:300px}
  .day-head{height:48px;border-radius:18px 18px 0 0;text-align:center;padding-top:6px;line-height:1}
  .day-head h2{font-size:19px;font-weight:700}
  .day-head p{font-size:9.5px;font-weight:600;margin-top:3px;line-height:1.15}
  .day--fri .day-head{background:var(--fri);color:var(--ink)}
  .day--sat .day-head{background:var(--sat);color:var(--white)}
  .day--sun .day-head{background:var(--sun);color:var(--white)}
  .day-grid{position:relative;height:432px;margin-top:5px;
    background-image:repeating-linear-gradient(180deg,transparent 0 26px,var(--line) 26px 27px)}
  .day--fri .day-grid{background-color:var(--fri)}
  .day--sat .day-grid{background-color:var(--sat)}
  .day--sun .day-grid{background-color:var(--sun)}
  .event{position:absolute;left:0;right:0;display:flex;flex-direction:column;justify-content:center;
    text-align:center;color:var(--white);font-size:8.5px;font-weight:600;line-height:1.2;
    text-transform:uppercase;border-top:1px solid var(--line);padding:1px 3px}
  .day--fri .event{background:var(--fri-event)}
  .day--sat .event{background:var(--sat-event)}
  .day--sun .event{background:var(--sun-event)}
  .event-name{font-size:9px}
  .brand{position:absolute;left:430px;top:40px;width:255px;text-align:center;
    font-size:34px;font-weight:700;line-height:1;color:var(--logo);text-transform:uppercase}
  .brand-dot{display:inline-block;width:14px;height:14px;border-radius:50%;background:var(--logo);margin-bottom:6px}
  .ship-art{position:absolute;left:430px;top:180px;width:265px;height:250px;border-radius:10px;
    background:linear-gradient(180deg,rgba(255,255,255,.25),var(--ship) 75%)}
</style>
</head>
<body>
<main class="schedule-board">
  <div class="waves" role="img" aria-label="Decorative blue ocean waves along the bottom"></div>

  <div class="time-rail">
    <div class="time-tag"><span>10 am</span></div>
    <div class="time-tag"><span>11 am</span></div>
    <div class="time-tag"><span>12 pm</span></div>
    <div class="time-tag"><span>1 pm</span></div>
    <div class="time-tag"><span>2 pm</span></div>
    <div class="time-tag"><span>3 pm</span></div>
    <div class="time-tag"><span>4 pm</span></div>
    <div class="time-tag"><span>5 pm</span></div>
    <div class="time-tag"><span>6 pm</span></div>
    <div class="time-tag"><span>7 pm</span></div>
    <div class="time-tag"><span>8 pm</span></div>
    <div class="time-tag"><span>9 pm</span></div>
    <div class="time-tag"><span>10 pm</span></div>
    <div class="time-tag"><span>11 pm</span></div>
    <div class="time-tag"><span>12 am</span></div>
    <div class="time-tag"><span>1 am</span></div>
  </div>

  <section class="day day--fri">
    <header class="day-head"><h2>FRIDAY</h2><p>LEAVE PORT<br>SPORTS DAY</p></header>
    <div class="day-grid">
      <div class="event" style="top:108px;height:66px">Hospitality Table<br>Pickup Wristbands<br>Meet &amp; Greets<br>Avant-Garde</div>
      <div class="event" style="top:196px;height:26px">Sail Away Party<br>Pool Deck</div>
      <div class="event" style="top:222px;height:26px">Country Atrium Party<br>Main Atrium Bar</div>
      <div class="event" style="top:248px;height:28px">Board Game Show<br>Paris Lounge</div>
      <div class="event" style="top:280px;height:52px">Lido Deck Party<br>Hank Sutter<br>&amp; Dancing</div>
      <div class="event" style="top:346px;height:20px">Adult Comedy Show</div>
      <div class="event" style="top:372px;height:36px">Travis Lee Holden<br>12:15am – Candlelight<br>Lounge</div>
    </div>
  </section>

  <section class="day day--sat">
    <header class="day-head"><h2>SATUR DAY</h2><p>PARTY AT SEA<br>CAMO DAY</p></header>
    <div class="day-grid">
      <div class="event" style="top:0;height:27px">Cody Harlan<br>10:00am</div>
      <div class="event" style="top:27px;height:30px">Wade Tillman – 11:15am<br>Candlelight Lounge</div>
      <div class="event" style="top:57px;height:30px">Dance Lesson &amp;<br>Dancing Avant-Garde</div>
      <div class="event" style="top:108px;height:62px">VIP Party 3pm–4pm<br>Jesse Marlow<br>Rhett Calder<br>Paris Lounge</div>
      <div class="event" style="top:200px;height:32px">6:00 – 10:00<br>Formal Diner</div>
      <div class="event" style="top:232px;height:34px">High Seas Karaoke<br>Avant-Garde</div>
      <div class="event" style="top:272px;height:26px">Country Atrium Party</div>
      <div class="event" style="top:298px;height:26px">Main Atrium Bar</div>
      <div class="event" style="top:324px;height:28px">Show: Steel Junction<br>10:15 – Paris Lounge</div>
      <div class="event" style="top:352px;height:20px">Adult Comedy Show</div>
      <div class="event" style="top:372px;height:36px">Colt Brennan<br>Hank Sutter<br>12:15am – Candlelight</div>
    </div>
  </section>

  <section class="day day--sun">
    <header class="day-head"><h2>SUN DAY</h2><p>ENCENADA<br>REDNECK DAY</p></header>
    <div class="day-grid">
      <div class="event" style="top:0;height:54px">8:00am – 5:00pm<br>Ensenada<br>DJ Tidewave<br>Mar Azul Cantina</div>
      <div class="event" style="top:54px;height:27px">11:00am<br>Wade Tillman</div>
      <div class="event" style="top:81px;height:27px">12:15pm<br>Colt Brennan</div>
      <div class="event" style="top:108px;height:36px">1:45pm<br>Travis Lee Holden</div>
      <div class="event" style="top:144px;height:27px">3:15pm<br>Rhett Calder</div>
      <div class="event" style="top:171px;height:45px">Dance Lesson &amp; Dancing<br>Avant-Garde Lounge<br>5–6:30pm</div>
      <div class="event" style="top:254px;height:42px">High Seas Karaoke<br>Avant-Garde</div>
      <div class="event" style="top:330px;height:32px">Mardi Gras Party<br>Main Atrium Bar</div>
      <div class="event" style="top:362px;height:46px">Jesse Marlow<br>Cody Harlan<br>12:15am – Candlelight</div>
    </div>
  </section>

  <h1 class="brand"><span class="brand-dot"></span><br>Coastal Country<br>Sail Fest</h1>

  <div class="ship-art" role="img" aria-label="Illustration of a cartoon cruise ship riding ocean waves"></div>
</main>
</body>
</html>
```